Harrowfield Nature Alliance needs a poster for fish fry

We need a flyer made for a fish fry. Things we need on it;

Date: Sunday, February 12th
Location: Brenmoor Sportsdome Auditorium
Time: 5-6:30 pm
Cost: $15 for adults, $10 for 12 & under, free for preschool

Requirements
Must have
• Must have our logo on it.

```html
<!DOCTYPE html>
<html lang="en">
<head>
<meta charset="utf-8">
<title>Fish Fry Poster – Harrowfield Nature Alliance</title>
<link rel="stylesheet" href="https://fonts.googleapis.com/css2?family=Anton&family=Cinzel:wght@700&family=Lilita+One&family=Poppins:wght@600;700&display=swap">
<style>
  :root {
    --page-bg: #e9e8e6;
    --wood-dark: #2a0f07;
    --wood-mid: #5a2412;
    --wood-light: #7a3a1d;
    --stripe: #d9742c;
    --sign-edge: #f3dbb3;
    --logo-tan: #dcb07c;
    --maroon: #7b1f1e;
    --ink: #2b1512;
    --gold: #e8b86a;
    --price-top: #f0622c;
    --price-bottom: #b8311a;
    --paper: #ffffff;
    --rule: #d6d3cf;
    --badge: #3a2a28;
  }
  * { margin: 0; padding: 0; box-sizing: border-box; }
  html, body { width: 1200px; height: 2741px; overflow: hidden; background: var(--page-bg); }
  .poster {
    position: absolute; left: 0; top: 522px; width: 1200px; height: 1696px;
    background: var(--paper); overflow: hidden;
    box-shadow: 0 20px 50px rgba(0,0,0,.25);
  }
  .wood-panel {
    position: absolute; left: 0; top: 0; width: 1200px; height: 1270px;
    background:
      repeating-linear-gradient(90deg, rgba(0,0,0,.07) 0 3px, transparent 3px 17px),
      radial-gradient(ellipse at 50% 25%, var(--wood-light) 0%, var(--wood-mid) 45%, var(--wood-dark) 100%);
  }
  .hanger { position: absolute; top: 0; width: 12px; height: 330px; background: var(--stripe); box-shadow: 0 0 8px rgba(0,0,0,.5); }
  .hanger--left { left: 258px; }
  .hanger--right { left: 916px; }
  .org-name {
    position: absolute; left: 0; width: 1200px; top: 150px; text-align: center;
    font-family: "Cinzel", serif; font-weight: 700; color: var(--logo-tan);
    font-size: 58px; line-height: 1.15; letter-spacing: 2px;
  }
  .org-name span { display: block; font-size: 30px; letter-spacing: 4px; }
  .food-photo {
    position: absolute; left: 280px; top: 610px; width: 640px; height: 640px;
    border-radius: 50%;
    background: radial-gradient(circle at 50% 50%, #c8652c 0%, #b5582a 38%, #9acb2c 52%, #86b52a 74%, #7c4a25 80%, #5e3318 100%);
    box-shadow: 0 12px 30px rgba(0,0,0,.45);
  }
  .title-sign { position: absolute; left: 112px; top: 312px; width: 976px; height: 330px; }
  .title-sign svg { position: absolute; inset: 0; }
  .presents {
    position: absolute; left: 0; width: 100%; top: 58px; text-align: center;
    font-family: "Poppins", sans-serif; font-weight: 700; font-size: 36px;
    letter-spacing: 14px; color: var(--ink);
  }
  .event-title {
    position: absolute; left: 0; width: 100%; top: 100px; text-align: center;
    font-family: "Lilita One", sans-serif; font-size: 160px; line-height: 1;
    color: var(--maroon); letter-spacing: 4px;
  }
  .torn-edge { position: absolute; left: 0; top: 1245px; width: 1200px; height: 40px; }
  .event-date {
    position: absolute; left: 184px; top: 1296px; width: 832px;
    font-family: "Anton", sans-serif; font-weight: 400; font-size: 90px; line-height: 1;
    color: var(--maroon); letter-spacing: 1px; white-space: nowrap;
  }
  .venue {
    position: absolute; left: 184px; top: 1397px; width: 567px; height: 66px;
    background: var(--ink); border-radius: 8px; color: var(--gold);
    font-family: "Anton", sans-serif; font-size: 33px; line-height: 66px;
    text-align: center; letter-spacing: .5px; white-space: nowrap;
  }
  .serving { position: absolute; left: 768px; top: 1396px; width: 252px; text-align: center; }
  .serving-label { font-family: "Poppins", sans-serif; font-weight: 700; font-size: 22px; color: var(--ink); line-height: 28px; }
  .serving-time {
    margin-top: 2px; background: var(--maroon); border-radius: 5px; color: var(--gold);
    font-family: "Anton", sans-serif; font-size: 29px; line-height: 40px;
  }
  .prices { position: absolute; left: 184px; top: 1504px; display: flex; gap: 33px; }
  .price { width: 166px; text-align: center; }
  .price-tag {
    height: 100px; border-bottom: 3px solid var(--rule);
    background: linear-gradient(var(--price-top), var(--price-bottom));
    color: #fff; font-family: "Lilita One", sans-serif; font-size: 70px; line-height: 100px;
  }
  .price-tag sup { font-size: 36px; vertical-align: 26px; }
  .price-tag--free { font-size: 48px; }
  .price-label { margin-top: 12px; font-family: "Poppins", sans-serif; font-weight: 600; font-size: 20px; color: var(--ink); white-space: nowrap; }
  .divider { position: absolute; left: 792px; top: 1470px; width: 2px; height: 160px; background: var(--rule); }
  .quality-badge {
    position: absolute; left: 845px; top: 1476px; width: 152px; height: 152px;
    border-radius: 50%; background: var(--badge);
  }
</style>
</head>
<body>
  <main class="poster">
    <section class="wood-panel">
      <div class="hanger hanger--left"></div>
      <div class="hanger hanger--right"></div>
      <div class="org-name">Harrowfield<span>Nature Alliance</span></div>
    </section>

    <div class="food-photo" role="img" aria-label="Fried fish steaks on a banana leaf in a wooden bowl with onion rings, lemon, peppercorns, basil and tomato"></div>

    <div class="title-sign">
      <svg viewBox="0 0 976 330" width="976" height="330" aria-hidden="true">
        <defs>
          <linearGradient id="signWood" x1="0" y1="0" x2="0" y2="1">
            <stop offset="0" stop-color="#eccb99"/>
            <stop offset=".5" stop-color="#d7a86d"/>
            <stop offset="1" stop-color="#c08950"/>
          </linearGradient>
        </defs>
        <path d="M70 18 Q488 -10 906 18 Q950 40 944 80 Q976 120 966 165 Q976 210 944 250 Q950 292 906 312 Q488 340 70 312 Q26 292 32 250 Q0 210 10 165 Q0 120 32 80 Q26 40 70 18 Z"
              fill="url(#signWood)" stroke="#f3dbb3" stroke-width="6"/>
      </svg>
      <div class="presents">PRESENTS</div>
      <div class="event-title">FISH FRY</div>
    </div>

    <svg class="torn-edge" viewBox="0 0 1200 40" preserveAspectRatio="none" aria-hidden="true">
      <path d="M0 22 L60 14 L120 24 L190 12 L260 22 L330 10 L400 20 L470 14 L540 24 L610 12 L680 20 L750 10 L820 22 L890 14 L960 24 L1030 12 L1100 20 L1200 14 L1200 40 L0 40 Z" fill="#ffffff"/>
    </svg>

    <h1 class="event-date">SUNDAY, FEBRUARY 12TH</h1>
    <div class="venue">BRENMOOR SPORTSDOME AUDITORIUM</div>
    <div class="serving">
      <div class="serving-label">SERVING STARTS AT</div>
      <div class="serving-time">5:00 PM-6:30 PM</div>
    </div>

    <div class="prices">
      <div class="price"><div class="price-tag"><sup>$</sup>15</div><div class="price-label">FOR ADULTS</div></div>
      <div class="price"><div class="price-tag"><sup>$</sup>10</div><div class="price-label">FOR 12 &amp; UNDER</div></div>
      <div class="price"><div class="price-tag price-tag--free">FREE</div><div class="price-label">FOR PRESCHOOL</div></div>
    </div>

    <div class="divider"></div>
    <div class="quality-badge" aria-hidden="true"></div>
  </main>
</body>
</html>
```